Legal Website Custom Template Design - Wordpress 3.0+

I need an original template designed in Wordpress (Wordpress 3.0+ compatible with widget support) for a legal website. The template should be designed so that 2 language versions of the same site can be supported at the same time (e.g., clicking on the language link on the upper right hand side will switch the content from English to another language). Also, the template should be flexible enough that I can add additional tabs, navigation as needed as part of the widgeting process.
The overall theme of my website should be to look simple, elegant, smart and professional.
I am envisioning 5 templates (see attached document for details of each tab and further project description).
6 tabs along the upper portion of the website, going left to right. There should be three different types of templates:
a. Home page (1st tab) that supports adds to the tabs on top for all pages.
b. Content page Level 1 (2nd tab (“Attorney/Staff Profiles”) and 3rd tab (“Practice Areas”)), general content with navigation that supports nearly unlimited adds to the left nav in terms of content areas.
c. Content page Level 2 (2nd tab (Actual bios of attorney/staff) and 3rd tab (Actual crimes and types of cases my firm handles)), deeper level.
d. Free Case Evaluation page (4th tab) that a potential client can easily fill ou.
e. FAQ Section page (5th tab), that has answers to questions a potential client may have.
f. .Contact Us page (6th tab) that I can easily place a contact us form.
There should also be a link on the homepage to a “Locate Us” page (Link), where I can place our address with Google Maps. This link will not be in the tabs sections up top. Currently, I’m thinking the link with a small icon for a map, will be near the bottom of the home page. Will need template for maps.
Please provide specific portfolio examples of Wordpress templates that you have created. Also note that once the project is complete, all intellectual property rights pertaining to this project will be owned by me.
Industry/Entity Type
Legal
Requirements
Must have
- Please see the attached word document.
Also, keep in mind the theme is simple, elegant, smart, and professional.

```html
<!DOCTYPE html>
<html lang="en">
<head>
<meta charset="utf-8">
<title>Reed Harlan Attorney</title>
<link href="https://fonts.googleapis.com/css2?family=PT+Sans:wght@400;700&display=swap" rel="stylesheet">
<style>
:root{
  --header-bg:#f3f3f3;
  --nav-dark:#1a1816;
  --nav-mid:#2b2825;
  --brown-deep:#241910;
  --brown:#352518;
  --brown-soft:#4a3322;
  --panel:#2e2118;
  --field:#5a402a;
  --orange:#e8891c;
  --gold:#f0a43a;
  --text-light:#e9e2d8;
  --text-muted:#a89a8a;
  --band-light:#f2f2f2;
  --ink:#222;
}
*{margin:0;padding:0;box-sizing:border-box}
html,body{width:800px;height:1200px;overflow:hidden}
body{font-family:"PT Sans",sans-serif;background:var(--brown-deep);position:relative;color:var(--text-light)}
.abs{position:absolute}

/* header */
.site-header{left:0;top:0;width:800px;height:118px;background:linear-gradient(#fdfdfd,var(--header-bg))}
.brand{left:28px;top:40px;display:flex;align-items:center;gap:12px}
.brand-mark{width:22px;height:22px;border-radius:50%;background:#c78a2a}
.brand-name{font-size:33px;color:#555;font-weight:400}
.language{left:626px;top:6px;font-size:12px;color:#444;display:flex;align-items:center;gap:6px}
.flag{width:16px;height:10px;display:inline-block}
.flag-en{background:#2a3f8c}
.flag-zh{background:#d0201c}
.search-box{left:534px;top:26px;width:246px;height:62px;border-radius:10px;background:linear-gradient(#fff,#dcdcdc);box-shadow:0 4px 8px rgba(0,0,0,.2)}
.search-input{left:14px;top:19px;width:156px;height:24px;border-radius:12px;background:#fff;border:1px solid #ccc}
.search-btn{left:172px;top:19px;width:60px;height:24px;border-radius:8px;background:#2b1f1c;color:#eee;font-size:12px;text-align:center;line-height:24px}

/* nav */
.page-bg{left:0;top:167px;width:800px;height:795px;background:radial-gradient(ellipse at 50% 40%,var(--brown-soft),var(--brown) 60%,var(--brown-deep))}
.main-nav{left:20px;top:118px;width:760px;height:49px;background:linear-gradient(var(--nav-mid),var(--nav-dark));display:flex;align-items:center}
.nav-item{font-size:12px;color:#f0f0f0;padding:0 22px;height:26px;line-height:26px;border-right:1px dotted #555}
.nav-item:last-child{border-right:none}
.nav-item.active{color:var(--orange)}
.dropdown{left:283px;top:167px;width:175px;height:108px;background:#1c1714;padding:4px 19px;z-index:3}
.dropdown div{font-size:12px;color:var(--gold);height:19.5px;line-height:19.5px}

/* slider */
.slider{left:20px;top:185px;width:760px;height:282px;border:1px solid #6a4a2a;background:linear-gradient(#1d1208 0%,#3a2410 55%,#5a3a14 70%,#1a0e06 100%)}
.slider-caption{left:49px;top:207px;width:215px;height:238px;background:rgba(70,40,15,.7);border:1px solid #6a4a2a;border-radius:4px}
.portrait{left:103px;top:227px;width:98px;height:120px;background:linear-gradient(#9aa4b0,#3d3a3c);border:2px solid #fff}
.caption-text{left:61px;top:357px;width:200px;font-size:13px;line-height:19.5px;color:var(--orange)}
.slide-arrow{top:298px;width:22px;height:44px;background:#111;color:#fff;font-size:14px;text-align:center;line-height:44px}
.slider-dots{left:706px;top:444px;display:flex;gap:2px}
.slider-dots span{width:15px;height:15px;border-radius:50%;background:#fff}
.slider-dots span:first-child{background:#d0700f}

/* side headings */
.side-heading{width:189px;height:28px;border-radius:4px;background:linear-gradient(#7a5535,#4a3020);border:1px solid #8a6545;color:var(--orange);font-size:15px;text-align:center;line-height:26px}
.form-field{left:31px;width:171px;background:var(--field);font-size:10px;color:#c8b8a5;padding:4px 14px;height:20px}
.submit-btn{left:73px;top:676px;width:74px;height:24px;border-radius:4px;background:#3a2818;color:var(--orange);font-size:10px;text-align:center;line-height:24px}

.welcome-title{left:281px;top:512px;color:var(--gold);font-size:15px}
.welcome-title b{font-size:20px;font-weight:400}
.welcome-rule{left:283px;top:548px;width:395px;height:1px;background:#8a6a4a}
.welcome-text{left:286px;top:569px;width:440px;font-size:10px;line-height:16.8px;color:#b5a695}

.news-item{left:25px;width:190px}
.news-date{left:0;top:0;width:62px;height:18px;background:#2a1408;color:#e0a060;font-size:10px;text-align:center;line-height:18px}
.news-text{left:68px;top:-5px;width:125px;font-size:10px;line-height:19.5px;color:var(--orange)}

.info-panel{top:730px;height:216px;background:rgba(30,20,12,.7)}
.panel-title{color:var(--orange);font-size:15px;position:absolute}
.panel-text{position:absolute;font-size:10px;line-height:19.5px;color:#eee}
.map{left:628px;top:777px;width:143px;height:155px;background:linear-gradient(135deg,#e8d8a8,#cdd6b8 60%,#9ec0de 75%);border-radius:3px}

/* features band */
.features{left:0;top:962px;width:800px;height:148px;background:var(--band-light);display:flex}
.feature{width:190px;text-align:center;position:relative;color:var(--ink)}
.feature+.feature{border-left:1px solid #bbb;margin:6px 0 8px}
.feature h3{font-weight:400;font-size:15px;margin-top:18px}
.feature p{font-size:10px;line-height:14px;position:absolute;left:0;right:0;top:104px}
.feature .icon{position:absolute;top:44px;left:50%;transform:translateX(-50%)}

/* footer */
.site-footer{left:0;top:1110px;width:800px;height:90px;background:linear-gradient(var(--brown),#1c130c)}
.social{left:24px;top:1142px;display:flex;gap:4px}
.social span{width:19px;height:19px;border-radius:50%}
.footer-links{left:265px;top:1136px;font-size:10px;color:#eee;word-spacing:1px}
.copyright{left:292px;top:1160px;font-size:10px;color:#eee}
.footer-brand{left:630px;top:1146px;display:flex;align-items:center;gap:8px;color:#7a6a5a;font-size:14px}
.footer-brand .brand-mark{width:14px;height:14px;background:#8a6a3a}
</style>
</head>
<body>

<header class="site-header abs">
  <div class="brand abs"><span class="brand-mark"></span><span class="brand-name">Reed Harlan Attorney</span></div>
  <div class="language abs">Language : <span class="flag flag-en" role="img" aria-label="English flag"></span><span class="flag flag-zh" role="img" aria-label="Chinese flag"></span></div>
  <div class="search-box abs">
    <div class="search-input abs"></div>
    <div class="search-btn abs">Search</div>
  </div>
</header>

<div class="page-bg abs"></div>

<nav class="main-nav abs">
  <span class="nav-item" style="padding-left:50px">Home</span>
  <span class="nav-item">Attorney / Staff Profiles</span>
  <span class="nav-item active">Practice Areas ⌄</span>
  <span class="nav-item">Free Case Evaluation</span>
  <span class="nav-item">FAQ Section</span>
  <span class="nav-item">Contact Us</span>
</nav>
<div class="dropdown abs">
  <div>Criminal Defense</div><div>Business Law</div><div>Immigration Law</div><div>Personal Injury</div><div>Estate Planning</div>
</div>

<section>
  <div class="slider abs" role="img" aria-label="Night city skyline reflected on water"></div>
  <div class="slide-arrow abs" style="left:22px">‹</div>
  <div class="slide-arrow abs" style="left:756px">›</div>
  <div class="slider-caption abs"></div>
  <div class="portrait abs" role="img" aria-label="Portrait of the attorney"></div>
  <p class="caption-text abs">Lorem ipsum dolor sit amet, consectetuer adipiscing elit. Nam nibh. Nunc varius facilisis eros. Sed erat.</p>
  <div class="slider-dots abs"><span></span><span></span><span></span><span></span></div>
</section>

<section>
  <div class="side-heading abs" style="left:20px;top:512px">Contact Form</div>
  <div class="form-field abs" style="top:550px">Name :</div>
  <div class="form-field abs" style="top:575px">Phone :</div>
  <div class="form-field abs" style="top:600px">Email :</div>
  <div class="form-field abs" style="top:624px;height:46px;padding-top:12px">Message :</div>
  <div class="submit-btn abs">Submit</div>

  <h1 class="welcome-title abs" style="font-weight:400">Welcome to <b>Reed Harlan Attorney</b></h1>
  <div class="welcome-rule abs"></div>
  <p class="welcome-text abs">When you and your family are enduring a difficult family law matter such as divorce, child custody or child support, it is important for you to have a sturdy shoulder to lean on. Attorney Calder has provided the residents of Long Beach with over a decade of her hardworking practice and experience, and she is ready to extend her services to you as well. Whether you are considering getting a divorce from your partner or you are in desperate need of a temporary order of protection, she is the attorney to call. She will work tirelessly on your case, trying to help you reach a desired outcome in the long run.</p>
</section>

<section>
  <div class="side-heading abs" style="left:20px;top:737px">Latest News</div>
  <div class="news-item abs" style="top:781px">
    <div class="news-date abs">22, sep.2011</div>
    <p class="news-text abs">Our features<br>We have a great number of successful cases, and our clients' testimonials...</p>
  </div>
  <div class="news-item abs" style="top:878px">
    <div class="news-date abs">22, sep.2011</div>
    <p class="news-text abs">Our features<br>We have a great number of successful cases, and our clients' testimonials...</p>
  </div>

  <div class="info-panel abs" style="left:236px;width:190px">
    <svg class="abs" style="left:18px;top:22px" width="30" height="24" viewBox="0 0 30 24"><path d="M2 2h26v15H12l-6 6v-6H2z" fill="#c8c0b0"/><text x="15" y="14" font-size="12" text-anchor="middle" fill="#333" font-family="serif">❝</text></svg>
    <div class="panel-title" style="left:60px;top:22px">Testimonials</div>
    <p class="panel-text" style="left:33px;top:62px">21 September, 2011</p>
    <p class="panel-text" style="left:33px;top:92px;width:150px">This is the place where you can see how your money works for you, simple and quite profitable.<br><br>Thank you.</p>
    <p class="panel-text" style="left:133px;top:169px;color:var(--orange)">viewmore</p>
  </div>
  <div class="info-panel abs" style="left:430px;width:180px">
    <div class="panel-title" style="left:55px;top:18px">Address</div>
    <p class="panel-text" style="left:43px;top:56px;width:120px">Lorem ipsum dolor sit amet, consectetuer adipiscing elit.</p>
    <p class="panel-text" style="left:8px;top:113px">Email : office@reedharlanlaw.example</p>
    <p class="panel-text" style="left:10px;top:140px">Phone: 000 111 4870</p>
  </div>
  <div class="info-panel abs" style="left:612px;width:174px">
    <div class="panel-title" style="left:51px;top:18px">Location Map</div>
  </div>
  <div class="map abs" role="img" aria-label="Street map showing the office location"></div>
</section>

<section class="features abs">
  <div class="feature" style="width:200px">
    <h3>Click to Call</h3>
    <svg class="icon" width="64" height="54" viewBox="0 0 64 54" role="img" aria-label="Phone"><rect x="6" y="22" width="52" height="28" rx="6" fill="#666"/><path d="M4 18c8-14 48-14 56 0l-8 6H12z" fill="#444"/><rect x="22" y="26" width="20" height="14" fill="#8ac"/></svg>
    <p>Connect to our office to<br>speak to an attorney</p>
  </div>
  <div class="feature" style="width:182px">
    <h3>Visit Our Blog</h3>
    <div class="icon" style="width:48px;height:60px;background:linear-gradient(#4cae3a,#2e7a22);border-radius:3px" role="img" aria-label="Book"></div>
    <p style="top:108px">Read helpful criminal<br>defense information</p>
  </div>
  <div class="feature" style="width:196px">
    <h3>Video Vault</h3>
    <div class="icon" style="width:56px;height:52px;background:linear-gradient(#5a6a8a,#222);border-radius:3px" role="img" aria-label="Video camera"></div>
    <p>Learn more about your<br>case from our videos</p>
  </div>
  <div class="feature" style="width:222px">
    <h3>Case Evaluation</h3>
    <svg class="icon" width="70" height="46" viewBox="0 0 70 46" role="img" aria-label="Envelope"><rect x="1" y="4" width="68" height="40" fill="#e6e6e6" stroke="#bbb"/><path d="M1 4l34 22 34-22" fill="none" stroke="#bbb"/></svg>
    <p>Fill out an online case<br>analysis form</p>
  </div>
</section>

<footer class="site-footer abs"></footer>
<div class="social abs" aria-label="Social links"><span style="background:#3b5a98"></span><span style="background:#3aa6d8"></span><span style="background:#1b7ab4"></span><span style="background:#e67a1c"></span></div>
<p class="footer-links abs">Privacy Policy &nbsp;| &nbsp;&nbsp;Contacts &nbsp;| &nbsp;&nbsp;Terms and conditions of use</p>
<p class="copyright abs">© 2011 Reed Harlan Attorney, All Rights Reserved</p>
<div class="footer-brand abs"><span class="brand-mark"></span>Reed Harlan Attorney</div>

</body>
</html>
```